依頼詳細
PCとスマホデザインの両方納品をいただきますが、
まずはデザインイメージが確認しやすいPCページのみの提案をお願いします。
スマホページは当選者に納品時にお願いしたいと思います。
スマホサイズについて、カンバスサイズは横幅375pxで作成し、2倍の横幅750pxのサイズで書き出ししてください。
(Retinaディスプレイに対応するため)
スマホページ作成時は、メニューが展開した際のデザインもお願いします。
レスポンシブウェブデザインを意識したデザインでお願いします。

■サイトマップ
添付の画面遷移図をご確認ください。

■参考サイト
https://www.hirotoku-sarumi.jp/
https://www.tabuse-seiban.co.jp/

■内容について
主に鋼材の卸売業を行う会社の公式サイトになります。
卸売だけでなく、鋼板を仕入れて希望のサイズに切断、プレスなどの加工も行う会社です。
参考サイトはメインビジュアルが動画になっていますが、今回のサイトデザインでは動画を使用する予定は今のところありません。

■素材写真
画像データについては、フリー素材から流用して
イメージ画像に当て込んでください。
足りない場合は、一旦他のサイトの写真をサンプルとして
入れてください。(サンプルなどの表記をお願いします)
また、購入が必要な写真などを利用した場合、
価格とサイト名を教えてください。

また、Pixoral Imageで定期契約をしていますので、
Pixoral Imageの画像は使用できます。
デザイン時はカンプ画像をお入れいただきますようお願いします。

■ロゴについて
添付のロゴデータを使用してください。

■ワイヤーフレーム
https://mock.velqara.net/view/52817caa-1f3b-4d0e-9a72-6e1b8c37d904-b39f/?fullscreen
コンテンツの構成としてワイヤーフレームを作成しましたが
必ずしもワイヤーフレームの通りではなくて大丈夫です。
TOPページに配置するコンテンツを見ていただき、デザインは
デザイナーの皆様におまかせしたいと思います。

----------------------------------------------------------------------------
【制作物に対するお願い】

■フォントについて
・無料で使えるフォントで作成をお願いします。
・OSに紐づくフォントの使用は控えていただければと思います (ヒラギノなど)

ページ数
1ページ
希望イメージ
シンプル 複雑
単色 カラフル
暗い 明るい
日常 高級
遊び心 厳粛
未来的 伝統的
女性的 男性的
希望する色
ベースカラー:白、青、ポイントカラー:赤
納品ファイル
• 高解像度JPG (.jpg)
• イラストレーター形式 (.ai)
• フォトショップ形式 (.psd)
補足説明
上記のいずれか1つ(アウトラインありとなしの2つ)と高解像度JPGを納品お願いします。
adobe XDでの納品も可能です。
CS5にバージョンを落としたロゴデータです。
ロゴのpngデータも追加しました。

```html
<!DOCTYPE html>
<html lang="ja">
<head>
<meta charset="utf-8">
<title>青嶺スチール株式会社</title>
<link href="https://fonts.googleapis.com/css2?family=Noto+Sans+JP:wght@400;500;700;900&family=Montserrat:wght@500;700&display=swap" rel="stylesheet">
<style>
:root{
  --navy:#0d2a86;
  --red:#d8192a;
  --ink:#222;
  --grey:#666;
  --faint:#ececec;
  --white:#fff;
}
*{margin:0;padding:0;box-sizing:border-box}
html,body{width:1200px;height:2804px;overflow:hidden}
body{position:relative;background:var(--white);font-family:"Noto Sans JP",sans-serif;color:var(--ink)}
a{text-decoration:none}
.abs,.ph{position:absolute}

/* header */
.brand{left:60px;top:30px;display:flex;align-items:center;gap:10px;font-weight:700;font-size:26px;color:var(--navy);letter-spacing:1px}
.brand-mark{width:16px;height:16px;background:var(--red)}
.nav{left:640px;top:44px;display:flex}
.nav a{font-size:15px;font-weight:500;color:var(--ink);padding:0 26px;border-left:1px solid #ccc}
.nav a:first-child{border-left:none}
.side-contact{right:0;top:340px;width:52px;height:140px;background:var(--red);color:var(--white);writing-mode:vertical-rl;font-size:14px;font-weight:700;display:flex;align-items:center;justify-content:center;letter-spacing:2px}

/* hero */
.hero-photo{left:160px;top:120px;width:1040px;height:580px;background:linear-gradient(135deg,#c9ced6,#7c8698 55%,#3a4358)}
.hero-panel{left:0;top:370px;width:1000px;height:330px;background:var(--navy);border-bottom-right-radius:40px;opacity:.92}
.hero-sub{left:170px;top:385px;font-size:40px;font-weight:700;color:var(--white)}
.hero-title{left:170px;top:450px;font-size:62px;font-weight:900;color:var(--white);letter-spacing:2px}
.hero-title small{font-size:40px}
.hero-tags{left:170px;top:548px;font-size:16px;font-weight:700;color:var(--white)}
.hero-tags span{background:var(--red);padding:6px 14px}

/* about */
.ghost{font-family:"Montserrat",sans-serif;font-weight:700;color:var(--faint);font-size:150px;line-height:1;letter-spacing:4px}
.ghost-about{left:100px;top:720px}
.sec-title{font-size:34px;font-weight:700;color:var(--navy)}
.about-title{left:420px;top:820px}
.about-photo{left:100px;top:900px;width:300px;height:620px;background:linear-gradient(160deg,#8a8f99,#3b4a6e 60%,#1e2c4f)}
.about-lead{left:600px;top:915px;font-size:22px;font-weight:700}
.about-body{left:600px;top:985px;width:500px;font-size:14px;line-height:2.1;color:var(--grey)}
.link{font-size:15px;font-weight:700;color:var(--ink);border-bottom:1px solid var(--ink);padding-bottom:10px;display:flex;justify-content:space-between;width:220px}
.link::after{content:"›";color:var(--red);font-size:18px}
.about-links{left:600px;top:1222px;display:flex;gap:40px}
.steel-photo{left:600px;top:1320px;width:500px;height:280px;background:linear-gradient(160deg,#c4c8cf,#5d6470 60%,#2b303a);border-bottom-left-radius:30px;z-index:2}

/* recruit */
.recruit-bg{left:380px;top:1360px;width:820px;height:740px;background:var(--navy)}
.ghost-recruit{left:440px;top:1680px;color:rgba(255,255,255,.12)}
.recruit-title{left:532px;top:1790px;color:var(--white)}
.recruit-body{left:532px;top:1870px;width:600px;font-size:14px;line-height:2.1;color:var(--white)}
.recruit-link{left:532px;top:1995px}
.recruit-link .link{color:var(--white);border-color:var(--white)}

/* strip */
.strip{left:0;top:2110px;width:1200px;height:250px;display:flex;gap:8px}
.strip div{flex:1;background:linear-gradient(160deg,#a7adb7,#4c5462 60%,#262c38)}

/* footer */
.footer{left:0;top:2420px;width:1200px;height:384px;background:var(--navy)}
.f-brand{left:60px;top:2490px;font-size:22px;color:var(--white)}
.f-brand .brand-mark{width:14px;height:14px}
.f-addr{left:60px;top:2535px;font-size:13px;line-height:2;color:var(--white)}
.f-note{left:480px;top:2488px;font-size:13px;color:var(--white)}
.f-tel{left:480px;top:2515px;display:flex;align-items:center;gap:10px;font-family:"Montserrat",sans-serif;font-weight:700;font-size:40px;color:var(--white)}
.f-hours{left:480px;top:2572px;font-size:12px;color:var(--white)}
.f-btn{left:852px;top:2488px;width:280px;height:120px;background:var(--red);color:var(--white);font-size:22px;font-weight:700;display:flex;align-items:center;justify-content:center;gap:12px}
.f-nav{left:120px;top:2665px;display:flex;gap:46px;font-size:13px;color:var(--white)}
.f-line{left:60px;top:2715px;width:1080px;height:1px;background:rgba(255,255,255,.25)}
.copy{left:0;top:2752px;width:1200px;text-align:center;font-size:11px;color:rgba(255,255,255,.8)}
</style>
</head>
<body>

<header>
  <div class="abs brand"><span class="brand-mark"></span>青嶺スチール株式会社</div>
  <nav class="abs nav"><a href="#">TOP</a><a href="#">事業内容</a><a href="#">会社概要</a><a href="#">採用情報</a></nav>
</header>

<section class="hero">
  <div class="ph hero-photo" role="img" aria-label="ヘルメットを持った作業着姿の社員4名が倉庫で並ぶ写真"></div>
  <div class="abs hero-panel"></div>
  <p class="abs hero-sub">わたしたちは、</p>
  <h1 class="abs hero-title">加工も手掛ける鋼材屋<small>です</small></h1>
  <p class="abs hero-tags"><span>鋼材一般販売 ／ 切断 ／ プレス ／ レーザー加工</span></p>
</section>

<a class="abs side-contact" href="#">お問い合わせ</a>

<section class="about">
  <div class="abs ghost ghost-about">ABOUT</div>
  <h2 class="abs sec-title about-title">青嶺スチールについて</h2>
  <div class="ph about-photo" role="img" aria-label="工場で鋼材を研磨する作業員の写真"></div>
  <p class="abs about-lead">テキストが入りますテキストが入ります</p>
  <p class="abs about-body">テキストが入りますテキストが入りますテキストが入りますテキストが入りますテキストが入りますテキストが入りますテキストが入りますテキストが入りますテキストが入りますテキストが入りますテキストが入りますテキストが入ります<br><br>テキストが入りますテキストが入りますテキストが入りますテキストが入りますテキストが入ります</p>
  <div class="abs about-links"><a class="link" href="#">事業内容</a><a class="link" href="#">会社概要</a></div>
</section>

<section class="recruit">
  <div class="abs recruit-bg"></div>
  <div class="ph steel-photo" role="img" aria-label="倉庫に積み重ねられた鋼板の写真"></div>
  <div class="abs ghost ghost-recruit">RECRUIT</div>
  <h2 class="abs sec-title recruit-title">採用情報</h2>
  <p class="abs recruit-body">テキストが入りますテキストが入りますテキストが入りますテキストが入りますテキストが入りますテキストが入りますテキストが入りますテキストが入りますテキストが入りますテキストが入りますテキストが入ります</p>
  <div class="abs recruit-link"><a class="link" href="#">採用情報</a></div>
</section>

<div class="abs strip">
  <div role="img" aria-label="工場内の作業風景の写真"></div>
  <div role="img" aria-label="加工機械の写真"></div>
  <div role="img" aria-label="鋼材を扱う作業員の写真"></div>
  <div role="img" aria-label="積まれた鋼材の写真"></div>
  <div role="img" aria-label="倉庫内の写真"></div>
</div>

<footer>
  <div class="abs footer"></div>
  <div class="abs brand f-brand"><span class="brand-mark"></span>青嶺スチール株式会社</div>
  <p class="abs f-addr">〒959-0000 青嶺市北町1丁目2-3<br>TEL 0479-22-8150　FAX 0479-22-8151</p>
  <p class="abs f-note">ご相談やお見積もりなど、お気軽にお問い合わせください。</p>
  <p class="abs f-tel"><svg width="30" height="30" viewBox="0 0 24 24" fill="#fff"><path d="M6.6 10.8a15 15 0 0 0 6.6 6.6l2.2-2.2a1 1 0 0 1 1-.25 11.4 11.4 0 0 0 3.6.57 1 1 0 0 1 1 1V20a1 1 0 0 1-1 1A17 17 0 0 1 3 4a1 1 0 0 1 1-1h3.5a1 1 0 0 1 1 1c0 1.25.2 2.45.57 3.57a1 1 0 0 1-.25 1z"/></svg>0479-22-8150</p>
  <p class="abs f-hours">受付時間 9:00〜17:00（土日祝除く）</p>
  <a class="abs f-btn" href="#"><svg width="26" height="20" viewBox="0 0 26 20" fill="none" stroke="#fff" stroke-width="2"><rect x="1" y="1" width="24" height="18"/><path d="M1 1l12 10L25 1"/></svg>お問い合わせ</a>
  <nav class="abs f-nav"><span>TOPページ</span><span>事業内容</span><span>会社概要</span><span>採用情報</span><span>お問い合わせ</span><span>プライバシーポリシー</span><span>サイトマップ</span></nav>
  <div class="abs f-line"></div>
  <p class="abs copy">Copyright © 青嶺スチール All Rights Reserved.</p>
</footer>

</body>
</html>
```